Consultants Need a Powerful New Image to Support a New Concept

We need a better image for an idea we have. Will be used in powerpoint but also in print (workbooks, handouts etc). The notion is that in any moment people in an organisation can choose to tell positive stories about what is going well, what they enjoy, what they are hopeful for or negative stories about what is wrong, not working or they are frustrated and pissed off about.

Target Market(s)

Leaders in organisations

Industry/Entity Type

It Support

Font styles to use
Sans Serif

Requirements
Must have
• The ability to build the image in powerpoint (at least add the text). Needs also to be used as a stand alone. Font and palette consistency with other materials. Some examples attached as well as font files and colour guidelines. Notice the left hand side of the model is about tell the stories and the right hand side is about how telling positive stories encourages others to seek more positive stories. On the right hand side down the bottom, the point is that these negative stories are so easy to join in on and they spread quickly and breed cynicism. Note the "Storyline" running up and down the middle - storyline model attached.
Nice to have
• A sense of momentum both up and down - the more positive stories we tell the more the organisation is energised and positive, the more negative stories (whingeing and complaining) the worse it is.

```html
<!DOCTYPE html>
<html lang="en">
<head>
<meta charset="utf-8">
<title>The Conversational Moment – Storyline Model</title>
<link href="https://fonts.googleapis.com/css2?family=Varela+Round&family=Montserrat:wght@800&display=swap" rel="stylesheet">
<style>
  :root {
    --blue: #0a6cb8;
    --blue-deep: #003a66;
    --blue-light: #29abe2;
    --blue-ink: #0b5ea8;
    --navy-line: #0d2f52;
    --red: #f01414;
    --red-deep: #4a0000;
    --red-ink: #d6141c;
    --red-line: #b3121a;
    --white: #ffffff;
    --ink: #111111;
    --scene-a: #d9dee6;
    --scene-b: #9fb6cf;
  }
  html, body {
    margin: 0;
    padding: 0;
    width: 1200px;
    height: 1200px;
    overflow: hidden;
    background: var(--white);
  }
  .storyline-model {
    display: block;
    width: 1200px;
    height: 1200px;
  }
  .band-positive { fill: var(--blue); }
  .band-negative { fill: var(--red); }
  .fold-positive { fill: var(--blue-deep); }
  .fold-negative { fill: var(--red-deep); }
  .band-text {
    font-family: "Varela Round", "Arial Rounded MT Bold", sans-serif;
    font-size: 22px;
    fill: var(--white);
    letter-spacing: 0.3px;
  }
  .banner-text { font-size: 25px; }
  .stage-label {
    font-family: "Varela Round", "Arial Rounded MT Bold", sans-serif;
    font-size: 32px;
    font-weight: 700;
    text-anchor: middle;
    letter-spacing: 1px;
  }
  .stage-positive { fill: var(--blue-light); }
  .stage-negative { fill: var(--red-ink); }
  .bubble-positive { fill: var(--white); stroke: var(--navy-line); stroke-width: 4; stroke-linejoin: round; }
  .bubble-negative { fill: var(--white); stroke: var(--red-line); stroke-width: 4; stroke-linejoin: round; }
  .bubble-text {
    font-family: "Varela Round", "Arial Rounded MT Bold", sans-serif;
    font-size: 20px;
    font-weight: 700;
  }
  .bubble-text-positive { fill: var(--blue-ink); }
  .bubble-text-negative { fill: var(--red-ink); }
  .moment-title {
    font-family: "Montserrat", "Arial Black", sans-serif;
    font-weight: 800;
    font-size: 31px;
    text-anchor: middle;
    fill: var(--ink);
    stroke: var(--white);
    stroke-width: 5;
    paint-order: stroke;
    letter-spacing: 0.5px;
  }
</style>
</head>
<body>
<svg class="storyline-model" viewBox="0 0 1500 1500" xmlns="http://www.w3.org/2000/svg">
  <defs>
    <linearGradient id="scene-fill" x1="0" y1="0" x2="1" y2="1">
      <stop offset="0" stop-color="var(--scene-a)"/>
      <stop offset="1" stop-color="var(--scene-b)"/>
    </linearGradient>
    <path id="path-banner-top" d="M590,182 Q750,148 912,182"/>
    <path id="path-bee-positive" d="M445,400 Q750,165 1065,400"/>
    <path id="path-see-positive" d="M425,590 Q750,225 1070,588"/>
    <path id="path-see-negative" d="M425,945 Q750,1305 1070,945"/>
    <path id="path-bee-negative" d="M432,1130 Q750,1360 1065,1130"/>
    <path id="path-banner-bottom" d="M590,1372 Q750,1389 912,1372"/>
  </defs>

  <g class="storyline-up">
    <path class="fold-positive" d="M600,222 Q830,175 1085,385 L1045,425 Q850,245 640,236 Z"/>
    <path class="fold-positive" d="M420,380 L470,425 Q600,378 760,392 Q610,368 470,372 Z"/>
    <path class="fold-positive" d="M740,440 Q960,455 1048,598 L1092,575 Q960,420 760,400 Z"/>

    <path class="band-positive" d="M570,140 Q750,100 928,140 L903,222 Q750,192 597,222 Z"/>
    <path class="band-positive" d="M420,380 Q750,140 1085,385 L1045,425 Q750,200 470,425 Z"/>
    <path class="band-positive" d="M402,578 Q750,170 1092,575 L1048,598 Q750,280 448,600 Z"/>

    <text class="band-text banner-text"><textPath href="#path-banner-top" startOffset="50%" text-anchor="middle" dominant-baseline="middle">Supports Performance</textPath></text>
    <text class="band-text"><textPath href="#path-bee-positive" startOffset="50%" text-anchor="middle" dominant-baseline="middle">Builds Confidence  ←  Encourages Proactive Behaviour  ↑</textPath></text>
    <text class="band-text"><textPath href="#path-see-positive" startOffset="50%" text-anchor="middle" dominant-baseline="middle">↗  Changes Awareness  →  Gives Insight, Shapes Beliefs  ↘</textPath></text>

    <text class="stage-label stage-positive" x="742" y="99">GET</text>
    <text class="stage-label stage-positive" x="742" y="239">DO</text>
    <text class="stage-label stage-positive" x="742" y="353">BEE</text>
    <text class="stage-label stage-positive" x="742" y="470">SEE</text>
  </g>

  <g class="storyline-down">
    <path class="fold-negative" d="M1045,935 Q920,1080 680,1098 L720,1150 Q960,1125 1092,955 Z"/>
    <path class="fold-negative" d="M468,1108 Q590,1100 700,1106 L705,1155 Q570,1150 468,1108 Z"/>
    <path class="fold-negative" d="M1045,1105 Q900,1290 598,1318 L905,1330 Q1010,1250 1085,1155 Z"/>

    <path class="band-negative" d="M402,955 Q750,1350 1092,955 L1048,935 Q750,1260 445,935 Z"/>
    <path class="band-negative" d="M445,1110 Q750,1320 1045,1105 L1085,1155 Q750,1400 420,1150 Z"/>
    <path class="band-negative" d="M583,1318 Q750,1336 910,1318 L928,1397 Q750,1429 570,1397 Z"/>

    <text class="band-text"><textPath href="#path-see-negative" startOffset="50%" text-anchor="middle" dominant-baseline="middle">↘  Fuels Unhelpful Beliefs  →  Builds Negative energy  ↗</textPath></text>
    <text class="band-text"><textPath href="#path-bee-negative" startOffset="50%" text-anchor="middle" dominant-baseline="middle">Destroys Confidence  →  Discourages Effort and Action</textPath></text>
    <text class="band-text"><textPath href="#path-banner-bottom" startOffset="50%" text-anchor="middle" dominant-baseline="middle">Undermines Performance</textPath></text>

    <text class="stage-label stage-negative" x="742" y="1066">SEE</text>
    <text class="stage-label stage-negative" x="742" y="1197">BEE</text>
    <text class="stage-label stage-negative" x="742" y="1306">DO</text>
    <text class="stage-label stage-negative" x="742" y="1457">GET</text>
  </g>

  <g class="conversational-moment">
    <rect x="585" y="612" width="345" height="268" rx="40" fill="url(#scene-fill)" role="img" aria-label="Two office colleagues talking: one worried in a grey shirt, one cheerful in a blue suit pointing upward"/>

    <g class="bubble tell-positive" transform="rotate(-11 645 570)">
      <rect class="bubble-positive" x="555" y="518" width="190" height="102" rx="12"/>
      <path class="bubble-positive" d="M680,614 L737,700 L712,614"/>
      <text class="bubble-text bubble-text-positive">
        <tspan x="569" y="546">TELL STORIES:</tspan>
        <tspan x="569" y="572">Bright Spots &amp;</tspan>
        <tspan x="569" y="598">Possibility</tspan>
      </text>
    </g>

    <g class="bubble seek-positive" transform="rotate(9 865 545)">
      <rect class="bubble-positive" x="765" y="492" width="218" height="102" rx="12"/>
      <path class="bubble-positive" d="M880,588 L900,681 L910,588"/>
      <text class="bubble-text bubble-text-positive">
        <tspan x="778" y="520">SEEK STORIES:</tspan>
        <tspan x="778" y="546">Catch People</tspan>
        <tspan x="778" y="572">Doing Things Right</tspan>
      </text>
    </g>

    <g class="bubble tell-negative" transform="rotate(-9 580 945)">
      <rect class="bubble-negative" x="495" y="895" width="172" height="100" rx="12"/>
      <path class="bubble-negative" d="M565,901 L630,755 L590,901"/>
      <text class="bubble-text bubble-text-negative">
        <tspan x="508" y="923">TELL STORIES:</tspan>
        <tspan x="508" y="949">Complaint &amp;</tspan>
        <tspan x="508" y="975">Failure</tspan>
      </text>
    </g>

    <g class="bubble join-negative" transform="rotate(4 850 955)">
      <rect class="bubble-negative" x="765" y="890" width="172" height="130" rx="12"/>
      <path class="bubble-negative" d="M800,896 L693,790 L830,896"/>
      <text class="bubble-text bubble-text-negative">
        <tspan x="778" y="917">JOIN STORIES:</tspan>
        <tspan x="778" y="943">Cynicism, Sar-</tspan>
        <tspan x="778" y="969">casm &amp; Nega-</tspan>
        <tspan x="778" y="995">tivity</tspan>
      </text>
    </g>

    <text class="moment-title" x="742" y="797">THE CONVERSATIONAL</text>
    <text class="moment-title" x="742" y="832">MOMENT</text>
  </g>
</svg>
</body>
</html>
```